New world-class investment firm needs a business card design

We need a business card design for a new investment firm called 'Ashgrove Hale Partners.' We acquire companies in the media sector and secure funding from conservative ultra, high-net worth individuals. We would like a black and white color design. We are seeking classic, elegant, and sophisticated designs. The final design should communicate financial safety, class, timelessness, and highly ethical. On the back of the business card, we would simply like the lion logo to be centered. I have attached a mock card, and variations on it are welcomed.
Industry/Entity Type
Conservative
Font styles to use
Other font styles liked:
- Garamond
Look and feel
Each slider illustrates characteristics of the customer's brand and the style your logo design should communicate.

```html
<!DOCTYPE html>
<html lang="en">
<head>
<meta charset="utf-8">
<title>Ashgrove Hale Partners — Business Card</title>
<link href="https://fonts.googleapis.com/css2?family=EB+Garamond:wght@400;500;600&display=swap" rel="stylesheet">
<style>
  :root {
    --backdrop: #2a2f32;
    --paper: #f6f5f1;
    --ink: #141414;
    --ink-soft: #3a3a3a;
    --band: #0d0d0d;
  }
  * { margin: 0; padding: 0; box-sizing: border-box; }
  html, body { width: 1200px; height: 1000px; overflow: hidden; }
  body {
    background: var(--backdrop);
    font-family: "EB Garamond", Garamond, serif;
    color: var(--ink);
    display: flex;
    flex-direction: column;
    align-items: center;
    justify-content: center;
    gap: 40px;
  }
  .card {
    width: 700px;
    height: 400px;
    background: var(--paper);
    position: relative;
    overflow: hidden;
  }
  /* Front */
  .card-front .brand {
    position: absolute;
    left: 44px;
    top: 46px;
    display: flex;
    align-items: center;
    gap: 20px;
  }
  .brand-circle { width: 84px; height: 84px; flex: none; }
  .brand-name {
    font-size: 34px;
    font-weight: 600;
    line-height: 0.95;
    text-transform: uppercase;
    letter-spacing: 0.5px;
  }
  .brand-cities {
    margin-top: 8px;
    padding: 3px 0;
    border-top: 1.5px solid var(--ink);
    border-bottom: 1.5px solid var(--ink);
    font-size: 13px;
    letter-spacing: 1px;
    text-transform: uppercase;
    white-space: nowrap;
  }
  .contact {
    position: absolute;
    left: 148px;
    top: 220px;
  }
  .contact-name { font-size: 26px; font-weight: 600; line-height: 1.1; }
  .contact-title { font-size: 14px; color: var(--ink-soft); margin-bottom: 14px; }
  .contact-line { font-size: 17px; line-height: 1.4; }
  .side-band {
    position: absolute;
    right: 0;
    top: 0;
    width: 120px;
    height: 100%;
    background: var(--band);
  }
  /* Back */
  .card-back {
    display: flex;
    flex-direction: column;
    align-items: center;
    justify-content: center;
    gap: 16px;
  }
  .back-circle { width: 110px; height: 110px; }
  .back-name {
    font-size: 22px;
    font-weight: 600;
    letter-spacing: 2px;
    text-transform: uppercase;
  }
</style>
</head>
<body>

  <section class="card card-front" aria-label="Business card front">
    <div class="brand">
      <svg class="brand-circle" viewBox="0 0 84 84" aria-hidden="true">
        <circle cx="42" cy="42" r="40" fill="none" stroke="var(--ink)" stroke-width="3"/>
      </svg>
      <div class="brand-text">
        <div class="brand-name">Ashgrove Hale<br>Partners</div>
        <div class="brand-cities">Boston • Chicago • Zurich</div>
      </div>
    </div>

    <div class="contact">
      <div class="contact-name">Julian T. Whitcombe</div>
      <div class="contact-title">Chairman &amp; CEO</div>
      <div class="contact-line">julian@ashgrovehale.com</div>
      <div class="contact-line">617 555 0142</div>
    </div>

    <div class="side-band" role="img" aria-label="Black band with a faint emblem pattern"></div>
  </section>

  <section class="card card-back" aria-label="Business card back">
    <svg class="back-circle" viewBox="0 0 110 110" aria-hidden="true">
      <circle cx="55" cy="55" r="52" fill="none" stroke="var(--ink)" stroke-width="3"/>
    </svg>
    <div class="back-name">Ashgrove Hale Partners</div>
  </section>

</body>
</html>
```